Cedar Bend Remedy Barn Label

I am looking to make a trendy and classy look for a label for our CBD products that's going on a green bottle and would like the writing on the label to be white I want a rustic farm look using different shades of green , I would like to keep it as Country Texas with the hipster flare as possible. I would like to keep it professional but look cool. I would like to incorporate the cross somewhere in there. We need room for nutriticianal facts info about the product i.e size of bottle fl , mg, and a qr code

```html
<!DOCTYPE html>
<html lang="en">
<head>
<meta charset="UTF-8">
<title>Cedar Bend Remedy Barn – CBD Oil Label</title>
<link rel="stylesheet" href="https://fonts.googleapis.com/css2?family=Oswald:wght@300;400;500;700&family=Dancing+Script:wght@700&display=swap">
<style>
  :root {
    --page: #ffffff;
    --band: #26374a;
    --band-edge: #2c4055;
    --panel: #ffffff;
    --ink: #24384c;
    --lime: #7db334;
    --leaf: #2f6a2c;
    --badge-ring: #ffffff;
    --muted: #6d7c8a;
    --light: #ffffff;
  }
  * { margin: 0; padding: 0; box-sizing: border-box; }
  html, body { width: 1200px; height: 900px; overflow: hidden; background: var(--page); }
  .canvas { position: relative; width: 1200px; height: 900px; }

  .label-band {
    position: absolute; left: 200px; top: 188px; width: 800px; height: 525px;
    background: var(--band);
  }
  .label-band__texture {
    position: absolute; inset: 0;
    background: linear-gradient(135deg, var(--band-edge), var(--band) 60%);
  }

  .info-panel {
    position: absolute; left: 242px; top: 0; width: 316px; height: 420px;
    background: var(--panel);
    text-align: center; color: var(--ink);
  }
  .info-panel::before, .info-panel::after {
    content: ""; position: absolute; top: 0; bottom: 0; width: 6px;
    background: radial-gradient(circle at center, var(--band) 3px, transparent 3.5px) 0 0 / 6px 10px repeat-y;
  }
  .info-panel::before { left: -3px; }
  .info-panel::after { right: -3px; }
  .info-panel__bottom-edge {
    position: absolute; left: 0; right: 0; bottom: -3px; height: 6px;
    background: radial-gradient(circle at center, var(--band) 3px, transparent 3.5px) 0 0 / 10px 6px repeat-x;
  }

  .brand-mark {
    position: absolute; left: 50%; top: 24px; width: 62px; height: 62px;
    margin-left: -31px; border-radius: 50%; background: var(--lime);
  }
  .brand-est {
    position: absolute; top: 110px; font: 400 9px/1 'Oswald', sans-serif;
    color: var(--muted); letter-spacing: 1px;
  }
  .brand-est--left { left: 24px; }
  .brand-est--right { right: 24px; }
  .brand-name {
    position: absolute; left: 0; right: 0; top: 98px;
    font: 500 26px/1.1 'Oswald', sans-serif; color: var(--ink);
    text-transform: uppercase; letter-spacing: 0.5px;
  }
  .brand-name span { display: block; }
  .brand-location {
    position: absolute; left: 0; right: 0; top: 158px;
    font: 400 11px/1 'Oswald', sans-serif; letter-spacing: 4px;
    color: var(--ink); text-transform: uppercase;
  }
  .brand-location .cross { color: var(--lime); font-weight: 700; }

  .product-name {
    position: absolute; left: 0; right: 0; top: 176px;
    font: 700 62px/1 'Oswald', sans-serif; color: var(--ink);
    letter-spacing: 1px;
  }
  .product-rule {
    position: absolute; left: 30px; right: 30px; top: 252px;
    border-top: 1.5px solid var(--ink);
  }
  .product-spec {
    position: absolute; left: 0; right: 0; top: 258px;
    font: 300 18px/1 'Oswald', sans-serif; color: var(--ink); letter-spacing: 1.5px;
  }
  .product-tag {
    position: absolute; left: 0; right: 0; top: 282px;
    font-family: 'Dancing Script', cursive; font-weight: 700; color: var(--ink);
  }
  .product-tag__pct { display: block; font-size: 20px; line-height: 1; padding-left: 90px; }
  .product-tag__word { display: block; font-size: 44px; line-height: 1; margin-top: -2px; }

  .farm-badge {
    position: absolute; left: 345px; top: 345px; width: 110px; height: 110px;
    border-radius: 50%; background: var(--leaf);
    border: 4px solid var(--badge-ring);
    box-shadow: 0 0 0 3px var(--leaf);
  }
  .volume {
    position: absolute; left: 0; right: 0; top: 476px; text-align: center;
    font: 300 15px/1 'Oswald', sans-serif; color: var(--light); letter-spacing: 1px;
  }
</style>
</head>
<body>
<main class="canvas">
  <section class="label-band">
    <div class="label-band__texture" role="img" aria-label="Subtle dark navy diagonal line pattern"></div>

    <div class="info-panel">
      <div class="brand-mark"></div>
      <span class="brand-est brand-est--left">EST.</span>
      <span class="brand-est brand-est--right">2016</span>
      <h1 class="brand-name"><span>Cedar Bend</span><span>Remedy Barn</span></h1>
      <p class="brand-location">Juniper Creek <span class="cross">+</span> Texas</p>
      <h2 class="product-name">CBD OIL</h2>
      <div class="product-rule"></div>
      <p class="product-spec">99% PURE ISOLATE</p>
      <p class="product-tag"><span class="product-tag__pct">100%</span><span class="product-tag__word">Natural</span></p>
      <div class="info-panel__bottom-edge"></div>
    </div>

    <div class="farm-badge" role="img" aria-label="Round green badge with sprout over farm fields and rising sun"></div>
    <p class="volume">1OZ / 30ml</p>
  </section>
</main>
</body>
</html>
```